Gestaltung von Honigetiketten
Zielgruppe
Ich bin ein Imker, der im eigenen Restaurant seinen Honig ausstellen und verkaufen möchte.
Aufgabenstellung
Ich möchte exklusive und edle Honigetiketten die auffallen. Bevorzugt mit den Farben Gold und Schwarz, siehe meinem bisher gesehenen Favoriten im Anhang.
Nur das Logo selbst (Baum) soll übernommen werden Farbe kann variieren, ebenso die Schrift ist variabel.
Auf die Vorderseite des Honigetiketts soll zu lesen sein:
- Deutscher Honig
- Sommertracht
- 500g
- Logo und Name
Auf der Rückseite des Honigetiketts soll zu finden sein:
- freies Feld für Stempel für Namen und Adresse des Abfüllers
- freies Feld für das Mindesthaltbarkeitsdatum

```html
<!DOCTYPE html>
<html lang="de">
<head>
<meta charset="utf-8">
<title>Sommertracht – Honigetikett</title>
<link href="https://fonts.googleapis.com/css2?family=Allura&family=Montserrat:wght@500;600;700&display=swap" rel="stylesheet">
<style>
  :root {
    --backdrop: #f1f0ed;
    --label-black: #0c0c0c;
    --comb-black: #161616;
    --gold: #c9a13a;
    --paper: #ffffff;
    --ink: #1a1a1a;
    --white-text: #f4f4f4;
  }
  html, body {
    margin: 0;
    width: 1200px;
    height: 732px;
    overflow: hidden;
    background: var(--backdrop);
  }
  .honey-label {
    display: block;
    width: 1200px;
    height: 732px;
  }
  .label-band, .front-panel { fill: var(--label-black); }
  .comb-texture { fill: var(--comb-black); }
  .gold-frame { fill: none; stroke: var(--gold); stroke-width: 1.2; }
  .stamp-field { fill: var(--paper); }
  .field-caption {
    font-family: "Montserrat", sans-serif;
    font-weight: 600;
    font-size: 4.6px;
    fill: var(--ink);
  }
  .brand-mark { fill: none; stroke: var(--gold); stroke-width: 1.6; }
  .brand-name {
    font-family: "Montserrat", sans-serif;
    font-weight: 600;
    font-size: 6px;
    letter-spacing: 1.2px;
    fill: var(--gold);
  }
  .product-name {
    font-family: "Allura", cursive;
    font-size: 44px;
    fill: var(--gold);
  }
  .product-type {
    font-family: "Montserrat", sans-serif;
    font-weight: 600;
    font-size: 12.5px;
    letter-spacing: 1.6px;
    fill: var(--gold);
  }
  .net-weight {
    font-family: "Montserrat", sans-serif;
    font-weight: 500;
    font-size: 10.5px;
    letter-spacing: 1.4px;
    fill: var(--white-text);
  }
</style>
</head>
<body>
<svg class="honey-label" viewBox="0 0 1200 732" xmlns="http://www.w3.org/2000/svg">
  <!-- wrap-around band -->
  <rect class="label-band" x="291" y="380" width="670" height="106"/>
  <rect class="comb-texture" x="410" y="383" width="420" height="100" role="img" aria-label="Dezentes Wabenmuster in Schwarz"/>
  <rect class="gold-frame" x="297" y="385" width="658" height="96"/>

  <!-- front diamond panel -->
  <polygon class="front-panel" points="615,322 492,400 492,466 615,548 738,466 738,400"/>
  <polyline class="gold-frame" points="523,385 615,328 707,385"/>
  <polyline class="gold-frame" points="523,481 614,542 707,481"/>

  <!-- back: filler stamp field -->
  <rect class="stamp-field" x="306" y="419" width="85" height="34"/>
  <text class="field-caption" x="311" y="426">Hergestellt und abgefüllt durch:</text>

  <!-- back: best-before field -->
  <rect class="stamp-field" x="863" y="418" width="85" height="36"/>
  <text class="field-caption" x="905.5" y="425" text-anchor="middle">Mindestens haltbar bis:</text>

  <!-- brand -->
  <circle class="brand-mark" cx="615" cy="384" r="22"/>
  <text class="brand-name" x="615" y="418" text-anchor="middle">GASTHOF AM BRUNNEN</text>

  <!-- product -->
  <text class="product-name" x="615" y="452" text-anchor="middle">Sommertracht</text>
  <text class="product-type" x="613" y="473" text-anchor="middle">DEUTSCHER HONIG</text>
  <text class="net-weight" x="612" y="517" text-anchor="middle">500 G</text>
</svg>
</body>
</html>
```